Poster to advertise new mind coaching clinic

Create a single sided A4 colour poster using the text provided. Suggested image provided. You may want to suggest an alternative however images need to appeal to both male and female sports people.

Text:
One-to-one mind coaching
For recreational and competitive sports people
Learn the mental tools and techniques used by the top sports people to fulfil your potential

 Create well-formed and achievable goals
 Overcome limiting beliefs
 Accelerate mastery through modelling your heroes
 Learn how to use mental rehearsal to increase your chances of success
 Smash through belief ceilings
 Get into the zone to bring your ‘A-Game’ more often
Thursdays in central Twyford
5-8pm
For more information contact:
thebluekitecoaching@postmere.com
Tel: 07481 265314
www.the-blue-kite.co.uk

Target Market(s)

sports people

Industry/Entity Type

Clinic

Requirements
Must have
• All the content provided. Contact details.

```html
<!DOCTYPE html>
<html lang="en">
<head>
<meta charset="utf-8">
<title>One-to-one Mind Coaching – Poster</title>
<link rel="stylesheet" href="https://fonts.googleapis.com/css2?family=Montserrat:wght@300;400;600;700;800&display=swap">
<style>
  :root {
    --paper: #ffffff;
    --ink: #2b2b2b;
    --charcoal: #3c3c3c;
    --charcoal-deep: #333333;
    --slate: #4d4d4d;
    --yellow: #f2c20f;
    --white: #ffffff;
    --rule: #c9c9c9;
  }
  * { box-sizing: border-box; margin: 0; padding: 0; }
  html, body { width: 744px; height: 1200px; overflow: hidden; background: var(--paper); }
  body { font-family: "Montserrat", Arial, sans-serif; color: var(--ink); }

  .poster { position: relative; width: 744px; height: 1200px; background: var(--paper); }

  /* Hero */
  .hero {
    position: absolute; left: 99px; top: 110px; width: 636px; height: 474px;
    overflow: hidden;
  }
  .hero-photo {
    position: absolute; inset: 0;
    background:
      radial-gradient(ellipse at 25% 40%, #9a8676 0%, rgba(90,78,70,0) 45%),
      radial-gradient(ellipse at 80% 40%, #a78f7c 0%, rgba(90,78,70,0) 40%),
      linear-gradient(180deg, #2e2c2c 0%, #4a4340 45%, #2a2828 100%);
  }
  .hero-title {
    position: absolute; left: 87px; top: 285px; width: 420px; height: 118px;
    border: 2px solid var(--white);
    background: rgba(30,30,30,0.35);
    color: var(--white); text-align: center;
  }
  .hero-title h1 {
    font-weight: 300; font-size: 58px; letter-spacing: 1px; line-height: 1;
    margin-top: 14px;
  }
  .hero-title p {
    font-weight: 400; font-size: 21px; letter-spacing: 3px; margin-top: 8px;
  }
  .hero-audience {
    position: absolute; left: 40px; top: 424px; width: 230px;
    color: var(--white); font-size: 14px; line-height: 1.25; font-weight: 400;
  }
  .hero-promise {
    position: absolute; left: 350px; top: 416px; width: 270px;
    color: var(--white); font-size: 14px; line-height: 1.25; font-weight: 400;
  }

  /* Benefits */
  .benefits-heading {
    position: absolute; left: 99px; top: 590px; width: 636px; text-align: center;
    font-size: 25px; font-weight: 400; letter-spacing: 0.5px; color: var(--ink);
  }
  .benefits-heading strong { font-weight: 800; }

  .benefits-chevrons { position: absolute; left: 99px; top: 632px; }

  .benefit-list { position: absolute; top: 622px; list-style: none; width: 236px; }
  .benefit-list.left { left: 194px; }
  .benefit-list.right { left: 452px; }
  .benefit {
    display: flex; align-items: flex-start; gap: 8px;
    height: 62px;
  }
  .benefit-num {
    color: var(--yellow); font-weight: 800; font-size: 30px; line-height: 1; width: 42px; flex: none;
  }
  .benefit-text {
    font-variant: small-caps; font-size: 12px; line-height: 1.2; color: var(--ink); padding-top: 2px;
  }
  .benefit-divider {
    position: absolute; left: 440px; top: 622px; width: 1px; height: 170px; background: var(--rule);
  }

  .brand {
    position: absolute; left: 598px; top: 776px;
    display: flex; align-items: center; gap: 6px;
    font-weight: 700; font-size: 16px; color: var(--ink);
  }
  .brand-dot { width: 12px; height: 12px; border-radius: 50%; background: var(--yellow); }

  /* Meeting point */
  .meeting {
    position: absolute; left: 99px; top: 806px; width: 636px; height: 290px; background: var(--charcoal);
  }
  .meeting-chevrons { position: absolute; left: 10px; top: 28px; }
  .meeting-title {
    position: absolute; left: 196px; top: 50px;
    color: var(--white); font-weight: 600; font-size: 40px; letter-spacing: 0.5px;
  }
  .meeting-when {
    position: absolute; left: 206px; top: 100px;
    color: var(--yellow); font-weight: 700; font-size: 14px; letter-spacing: 1px;
  }
  .meeting-time {
    position: absolute; left: 368px; top: 134px; width: 120px; height: 44px;
    background: var(--yellow); color: var(--charcoal-deep);
    font-weight: 800; font-size: 24px; text-align: center; line-height: 44px;
  }
  .contact-strip {
    position: absolute; left: 0; top: 208px; width: 636px; height: 50px; background: var(--yellow);
    display: flex; align-items: center; justify-content: space-between; padding: 0 20px;
    font-size: 11px; font-weight: 700; color: var(--charcoal-deep); letter-spacing: 0.2px;
  }
</style>
</head>
<body>
<main class="poster">

  <section class="hero">
    <div class="hero-photo" role="img" aria-label="Photograph of two athletes, a man lifting his shirt to show his abdomen and a woman in a sports top, in warm skin tones against a dark background"></div>
    <div class="hero-title">
      <h1>One-to-one</h1>
      <p>mind coaching</p>
    </div>
    <p class="hero-audience">For recreational and competitive sports people</p>
    <p class="hero-promise">Learn the mental tools and techniques used by the top sports people to fulfil your potential</p>
  </section>

  <h2 class="benefits-heading">ONE TO ONE <strong>MIND COACHING</strong></h2>

  <svg class="benefits-chevrons" width="80" height="146" viewBox="0 0 80 146" aria-hidden="true">
    <polygon points="0,0 28,0 64,73 28,146 0,146 36,73" fill="#f2c20f"/>
    <polygon points="28,0 44,0 80,73 44,146 28,146 64,73" fill="#4d4d4d"/>
  </svg>

  <ul class="benefit-list left">
    <li class="benefit"><span class="benefit-num">04</span><span class="benefit-text">Learn how to use mental rehearsal to increase your chances of success</span></li>
    <li class="benefit"><span class="benefit-num">05</span><span class="benefit-text">Smash through belief ceilings</span></li>
    <li class="benefit"><span class="benefit-num">06</span><span class="benefit-text">Get into the zone to bring your ‘A-Game’ more often</span></li>
  </ul>
  <div class="benefit-divider"></div>
  <ul class="benefit-list right">
    <li class="benefit"><span class="benefit-num">01</span><span class="benefit-text">Create well-formed and achievable goals</span></li>
    <li class="benefit"><span class="benefit-num">02</span><span class="benefit-text">Overcome limiting beliefs</span></li>
    <li class="benefit"><span class="benefit-num">03</span><span class="benefit-text">Accelerate mastery through modelling your heroes</span></li>
  </ul>

  <div class="brand"><span class="brand-dot"></span><span>Blue Kite</span></div>

  <section class="meeting">
    <svg class="meeting-chevrons" width="150" height="140" viewBox="0 0 150 140" aria-hidden="true">
      <polygon points="0,0 30,0 64,70 30,140 0,140 34,70" fill="#f2c20f"/>
      <polygon points="66,0 96,0 130,70 96,140 66,140 100,70" fill="#f2c20f"/>
    </svg>
    <h2 class="meeting-title">MEETING POINT</h2>
    <p class="meeting-when">THURSDAYS IN CENTRAL TWYFORD</p>
    <p class="meeting-time">5-8PM</p>
    <div class="contact-strip">
      <span>WWW.THE-BLUE-KITE.CO.UK</span>
      <span>TEL: 07481 265314</span>
      <span>THEBLUEKITECOACHING@POSTMERE.COM</span>
    </div>
  </section>

</main>
</body>
</html>
```